BRIGHTDESK - Remote Tech Support Site

We are looking for a new very responsive and simple website for our brand Brightdesk.com - a remote technical support company.

This company supports customers Globally in different countries throughout Eur/ North America / South America / Asia etc (please keep this in mind and integrate into the idea).

Its important to us that the design is very explanatory, the customer should easily be able to figure out that we provide computer support right away ... I like one page responsive type designs as well without a bunch of menu items

Here are some similar sites we like - but still looking for a unique design that fits out brand "brightdesk" - I have upload also some layouts i like (but the designs are not important just the layouts), youll see it includes consumer business etc which is important.

VOLM.COM - I love how clean it is - nice and white easy to see everything

PLUMWIRE247.COM - also nice the layout and responsive one page design makes it easy to use

corvalfix.com - similar to plumwire design as well - you can get the idea im looking for between the two

You will notice those examples are much different then the attachments I added - again this is more of an idea for possible layouts .. attached is also the logo - could inspire color scheme / blue white black etc

Target Market(s)

Home consumers without computer knowledge , older age 45-65, small medium business ... computer repair - slow computers

Industry/Entity Type

Computer Repair

Logo Text

Brightdesk

Coding

Coded - Design and coding required

Number of Pages Required

1 page

Font styles to use
Sans Serif
Other font styles liked:
• your choice responsive

Colors

Designer to choose colors to be used in the design.

Requirements
Must have
• Clean - responsive - professional design - the name says it all - brightdesk
• CALL TO ACTIONS FOR "Get Help Now!" / "Learn More" etc
Nice to have
• We are looking for a new very responsive and simple website for our brand Brightdesk.com - a remote technical support company.
• This company supports customers Globally in different countries throughout Eur/ North America / South America / Asia etc (please keep this in mind and integrate into the idea).
• Its important to us that the design is very explanatory, the customer should easily be able to figure out that we provide computer support right away ... I like one page responsive type designs as well without a bunch of menu items
• Here are some similar sites we like - but still looking for a unique design that fits out brand "brightdesk" - I have upload also some layouts i like (but the designs are not important just the layouts), youll see it includes consumer business etc which is important.
• VOLM.COM - I love how clean it is - nice and white easy to see everything
• PLUMWIRE247.COM - also nice the layout and responsive one page design makes it easy to use
• corvalfix.com - similar to plumwire design as well - you can get the idea im looking for between the two
Should not have
• dark, packed page - bad small font -

```html
<!DOCTYPE html>
<html lang="en">
<head>
<meta charset="utf-8">
<title>Brightdesk – Remote Tech Support</title>
<link href="https://fonts.googleapis.com/css2?family=Open+Sans:wght@400;600;700&display=swap" rel="stylesheet">
<style>
:root{
  --blue:#2b8ef0;
  --blue-dark:#1c74d4;
  --green:#2fc39d;
  --tick:#5cbf4a;
  --ink:#2b2f36;
  --muted:#8a9099;
  --line:#e3e7ec;
  --soft:#f3f5f8;
  --white:#ffffff;
}
*{box-sizing:border-box;margin:0;padding:0}
html,body{width:1200px;height:5172px;overflow:hidden}
body{font-family:"Open Sans",Arial,sans-serif;color:var(--ink);background:var(--white);position:relative}
section,header,footer,nav{position:absolute;left:0;width:1200px;overflow:hidden}
.abs{position:absolute}
.btn{display:inline-block;background:var(--blue);color:#fff;font-weight:700;font-size:16px;border-radius:22px;padding:12px 30px}
.btn-ghost{display:inline-block;border:1.5px solid var(--blue);color:var(--blue);font-size:13px;font-weight:600;border-radius:18px;padding:8px 26px}
.h2{font-size:22px;font-weight:700}
.small{font-size:12px;line-height:1.6;color:var(--muted)}
.photo{position:absolute}

/* top strip + hero */
.hero{top:0;height:670px}
.hero .photo{inset:0;background:linear-gradient(100deg,#cfd3d8 0%,#e4e6e9 35%,#c9ccd0 60%,#dadcdf 100%)}
.topbar{top:0;height:34px;background:rgba(255,255,255,.55);font-size:11px;color:var(--muted);padding:10px 30px}
.topbar span{margin-right:28px}
.hero-copy{left:240px;top:230px;width:420px}
.hero-copy h1{font-size:40px;font-weight:700;color:#222}
.hero-copy h3{font-size:24px;font-weight:600;color:#222;margin-top:2px}
.hero-copy p{font-size:13px;color:#444;line-height:1.55;margin:16px 0 22px;width:330px}

/* nav */
.nav{top:670px;height:70px;background:var(--blue);color:#fff}
.logo{left:52px;top:20px;font-size:24px;font-weight:600;display:flex;align-items:center;gap:8px}
.logo i{width:24px;height:24px;border-radius:50%;background:#fff;display:block}
.menu{right:52px;top:24px;display:flex;align-items:center;gap:30px;font-size:12px;font-weight:600}
.menu .login{border:1.5px solid #fff;border-radius:16px;padding:6px 32px}

/* about */
.about{top:740px;height:425px}
.about-copy{left:240px;top:70px;width:250px}
.about-copy .small{margin-top:18px;color:#555}
.about-frame{left:560px;top:85px;width:415px;height:245px;border:3px solid #e1e4e8}
.about .photo{left:538px;top:66px;width:413px;height:240px;background:linear-gradient(120deg,#e8ebef,#b8c1cb 50%,#8e99a6)}

/* realtime */
.realtime{top:1165px;height:405px}
.realtime .photo{inset:0;background:linear-gradient(90deg,#f7f8fa 0%,#eef1f5 40%,#9db2c8 75%,#6d87a3 100%)}
.realtime-copy{left:240px;top:60px;width:360px}
.realtime-copy h2{font-size:22px;font-weight:700;line-height:1.25}
.ticks{list-style:none;margin:20px 0 26px}
.ticks li{display:flex;align-items:center;gap:10px;font-size:13px;color:#555;margin-bottom:12px}
.ticks svg{flex:none}

/* features */
.features{top:1570px;height:642px}
.features .h2{position:absolute;top:85px;width:100%;text-align:center}
.card{position:absolute;width:235px;height:122px;background:#fff;border:1px solid var(--line);box-shadow:0 2px 6px rgba(0,0,0,.05);text-align:center;padding-top:14px}
.card .ic{width:28px;height:28px;border-radius:50%;background:var(--blue);margin:0 auto 8px}
.card b{font-size:13px;font-weight:600;display:block}
.card p{font-size:11px;color:var(--muted);line-height:1.5;margin:6px 22px 0}
.card.hl{box-shadow:0 6px 16px rgba(0,0,0,.12)}

/* how it works */
.how{top:2212px;height:618px;background:linear-gradient(160deg,#2b8ef0 0%,#2aa8d0 50%,#2fc39d 100%);color:#fff}
.how .h2{position:absolute;top:52px;width:100%;text-align:center}
.timeline{left:599px;top:130px;width:2px;height:420px;background:rgba(255,255,255,.7)}
.dot{width:14px;height:14px;border-radius:50%;background:#fff;border:3px solid var(--blue)}
.step{width:220px;font-size:11px;line-height:1.5;color:rgba(255,255,255,.9)}
.step b{display:block;font-size:13px;color:#fff;margin-bottom:4px}
.step.l{text-align:right}
.how .photo{width:225px;height:122px;border:4px solid #fff}

/* customers */
.customers{top:2830px;height:445px}
.cust-copy{left:240px;top:55px;width:230px}
.cust-copy .small{margin-top:14px;color:#777}
.quote{position:absolute;width:225px;height:120px;background:#fff;border:1px solid var(--line);box-shadow:0 2px 8px rgba(0,0,0,.08);padding:14px}
.quote p{font-size:11px;color:var(--muted);line-height:1.5}
.quote .who{display:flex;align-items:center;gap:8px;margin-top:14px;font-size:11px;font-weight:600}
.quote .who i{width:24px;height:24px;border-radius:50%;background:#3e4b5a;display:block}
.dots{left:492px;top:270px;display:flex;gap:6px}
.dots i{width:7px;height:7px;border-radius:50%;background:#cfd5dc}
.dots i.on{background:var(--blue)}
.stat{position:absolute;top:315px;width:180px;text-align:center}
.stat strong{display:block;font-size:44px;font-weight:400;color:var(--blue);line-height:1}
.stat span{font-size:16px;font-weight:700}

/* plans */
.plans{top:3275px;height:560px;background:var(--soft)}
.plans .h2{position:absolute;top:50px;width:100%;text-align:center}
.plan{position:absolute;top:125px;width:225px;height:320px;background:#fff;text-align:center;box-shadow:0 2px 8px rgba(0,0,0,.06)}
.plan.featured{top:105px;height:365px;box-shadow:0 8px 22px rgba(0,0,0,.15)}
.plan header{position:static;width:auto;background:var(--blue);color:#fff;font-size:12px;font-weight:700;padding:14px 0}
.plan .price{font-size:22px;font-weight:700;margin-top:16px}
.plan .sub{font-size:10px;color:var(--muted);margin-top:4px}
.plan .bar{width:50px;height:2px;background:var(--blue);margin:16px auto}
.plan ul{list-style:none;font-size:11px;color:#555;text-align:left}
.plan li{border-top:1px solid var(--line);padding:9px 16px}
.plan .btn-ghost{margin-top:18px;font-size:11px;padding:6px 22px}
.plan.featured .btn-ghost{background:var(--blue);color:#fff}
.pager{left:578px;top:500px;font-size:10px;color:var(--muted);border:1px solid #cfd5dc;padding:2px 10px}

/* video */
.video{top:3835px;height:223px}
.video .photo{inset:0;background:linear-gradient(90deg,#4e8fd9,#3f86e0 50%,#5c9be0)}
.play{left:568px;top:62px;text-align:center;color:#fff;font-size:13px;font-weight:600}

/* partners */
.partners{top:4058px;height:142px}
.partner{position:absolute;top:48px;width:160px;height:46px;display:flex;align-items:center;justify-content:center;gap:8px;font-size:16px;font-weight:600;color:#8d939b}
.partner i{width:16px;height:16px;border-radius:50%;background:#b9bec5;display:block}
.partner.boxed{border:1px solid #d5d9de;box-shadow:0 2px 8px rgba(0,0,0,.1)}

/* contact */
.contact{top:4200px;height:396px}
.contact .photo{inset:0;background:linear-gradient(135deg,#e6e8ea,#d7dadd 50%,#e2e4e6)}
.contact-card{left:240px;top:45px;width:225px;height:318px;background:#fff;box-shadow:0 4px 14px rgba(0,0,0,.12);padding:22px}
.contact-card h2{font-size:18px;font-weight:700}
.contact-card .small{margin:10px 0 12px;font-size:11px}
.line-item{display:flex;gap:8px;align-items:flex-start;font-size:11px;color:#555;margin-bottom:10px;line-height:1.4}
.line-item i{flex:none;width:12px;height:12px;border-radius:50%;background:var(--blue);margin-top:2px}
.socials{display:flex;gap:10px;justify-content:center;margin-top:10px}
.socials i{width:26px;height:26px;border-radius:50%;background:var(--blue);display:block}

/* form */
.form{top:4596px;height:274px}
.field{position:absolute;border:1px solid var(--line);font-size:11px;color:var(--muted);padding:9px 12px}
.send{left:540px;top:228px;width:170px;text-align:center;background:var(--blue);color:#fff;font-size:12px;font-weight:600;padding:8px 0}

/* subscribe */
.subscribe{top:4870px;height:240px;background:var(--blue);color:#fff;text-align:center}
.subscribe h2{margin-top:70px;font-size:22px;font-weight:700}
.subscribe p{font-size:11px;opacity:.85;margin:8px auto 0;width:420px;line-height:1.5}
.sub-input{left:370px;top:158px;width:460px;height:32px;border:1px solid rgba(255,255,255,.7);border-radius:16px;font-size:11px;text-align:left;padding:8px 16px}
.sub-btn{left:730px;top:158px;width:100px;height:32px;background:#fff;color:var(--blue);border-radius:16px;font-size:11px;font-weight:700;padding-top:8px}

.footer{top:5110px;height:62px;font-size:11px;color:var(--muted);text-align:center;padding-top:22px}
</style>
</head>
<body>

<header class="hero">
  <div class="photo" role="img" aria-label="Smiling older couple at a laptop receiving remote support"></div>
  <div class="topbar abs" style="left:0;width:1200px"><span>info@brightdesk.com</span><span>(555) 014-2280</span></div>
  <div class="hero-copy abs">
    <h1>Dedicated Support</h1>
    <h3>Anytime, Anywhere</h3>
    <p>Remote help for homes and businesses in Europe, the Americas and Asia, fixing slow computers fast.</p>
    <span class="btn">Get Help Now!</span>
  </div>
</header>

<nav class="nav">
  <div class="logo abs"><i></i>brightdesk</div>
  <div class="menu abs"><span>HOME</span><span>ABOUT US</span><span>SERVICES</span><span>CONTACT US</span><span>FAQs</span><span class="login">Login</span></div>
</nav>

<section class="about">
  <div class="about-copy abs">
    <h2 class="h2">ABOUT US</h2>
    <p class="small">Our team is a leader in providing top notch quality service and products with a focus on our customers' needs. We are happy to help you get your computer running again.</p>
    <p class="small">While you are looking for the best source out there, we are here providing the support you need.</p>
  </div>
  <div class="about-frame abs"></div>
  <div class="photo" role="img" aria-label="Support agents with headsets working at a help desk"></div>
</section>

<section class="realtime">
  <div class="photo" role="img" aria-label="Smiling technician working at a laptop in an office"></div>
  <div class="realtime-copy abs">
    <h2>Real-Time<br>Support Features &amp; Benifits</h2>
    <ul class="ticks">
      <li><svg width="16" height="16" viewBox="0 0 16 16"><circle cx="8" cy="8" r="8" fill="#5cbf4a"/><path d="M4.5 8.2l2.3 2.3 4.7-4.7" stroke="#fff" stroke-width="1.8" fill="none"/></svg>24/7 Real-Time Technical Support</li>
      <li><svg width="16" height="16" viewBox="0 0 16 16"><circle cx="8" cy="8" r="8" fill="#5cbf4a"/><path d="M4.5 8.2l2.3 2.3 4.7-4.7" stroke="#fff" stroke-width="1.8" fill="none"/></svg>The Best Security Software in the Market</li>
      <li><svg width="16" height="16" viewBox="0 0 16 16"><circle cx="8" cy="8" r="8" fill="#5cbf4a"/><path d="M4.5 8.2l2.3 2.3 4.7-4.7" stroke="#fff" stroke-width="1.8" fill="none"/></svg>Regular Tune-ups and Optimization</li>
      <li><svg width="16" height="16" viewBox="0 0 16 16"><circle cx="8" cy="8" r="8" fill="#5cbf4a"/><path d="M4.5 8.2l2.3 2.3 4.7-4.7" stroke="#fff" stroke-width="1.8" fill="none"/></svg>Setup and Installation Included</li>
    </ul>
    <span class="btn">Learn More</span>
  </div>
</section>

<section class="features">
  <h2 class="h2">Our Features</h2>
  <div class="card" style="left:240px;top:152px"><div class="ic"></div><b>Ad Blocker</b><p>Block pop-ups and ads for a faster, safer web.</p></div>
  <div class="card" style="left:483px;top:152px"><div class="ic"></div><b>Regular Tune-Ups</b><p>Keep your computer fast with regular tune-ups.</p></div>
  <div class="card hl" style="left:725px;top:152px"><div class="ic"></div><b>System Reports</b><p>Clear monthly reports on the health of your PC.</p></div>
  <div class="card" style="left:240px;top:306px"><div class="ic"></div><b>Identity Protection</b><p>Guard your personal data against online theft.</p></div>
  <div class="card" style="left:483px;top:306px"><div class="ic"></div><b>Mobile Security</b><p>Protect phones and tablets just like your PC.</p></div>
  <div class="card" style="left:725px;top:306px"><div class="ic"></div><b>Cross-Platform Support</b><p>Help for every major system, wherever you are.</p></div>
  <div class="card" style="left:362px;top:460px"><div class="ic"></div><b>Cloud Backup</b><p>Files stored safely in the cloud, easy to restore.</p></div>
  <div class="card" style="left:604px;top:460px"><div class="ic"></div><b>Multiple Devices</b><p>One plan covers every device at home or work.</p></div>
</section>

<section class="how">
  <h2 class="h2">How it Works</h2>
  <div class="timeline abs"></div>
  <div class="dot abs" style="left:593px;top:150px"></div>
  <div class="dot abs" style="left:593px;top:290px"></div>
  <div class="dot abs" style="left:593px;top:455px"></div>
  <div class="step l abs" style="left:355px;top:140px"><b>FREE Diagnostic</b>Get a diagnostic from our techs with a free consultation.</div>
  <div class="photo" style="left:635px;top:108px" role="img" aria-label="Hands typing on a laptop during diagnostics"></div>
  <div class="photo" style="left:345px;top:250px" role="img" aria-label="Laptop on a desk showing a support session"></div>
  <div class="step abs" style="left:625px;top:280px"><b>Get Fixed</b>Our technicians log in remotely and fix your computer issues right before your eyes.</div>
  <div class="step l abs" style="left:355px;top:445px"><b>Backup your Information</b>Keep your files safe with a secure backup so nothing is lost again.</div>
  <div class="photo" style="left:635px;top:418px" role="img" aria-label="Woman smiling while using a laptop"></div>
</section>

<section class="customers">
  <div class="cust-copy abs">
    <h2 class="h2">Our Customers</h2>
    <p class="small">Homes and small businesses around the world trust us to keep their computers fast and secure. Read what a few of them say about our friendly technicians and quick fixes for slow machines.</p>
  </div>
  <div class="quote" style="left:492px;top:80px"><p>Quick, patient help that made my old laptop feel new again. Highly recommended.</p><div class="who"><i></i>Mara Lind</div></div>
  <div class="quote" style="left:727px;top:80px"><p>The technician fixed our office network remotely in under an hour. Great service.</p><div class="who"><i></i>Jon Brekke</div></div>
  <div class="dots abs"><i class="on"></i><i></i><i></i></div>
  <div class="stat" style="left:243px"><strong>25000</strong><span>Customers</span></div>
  <div class="stat" style="left:414px"><strong>750</strong><span>Employees</span></div>
  <div class="stat" style="left:610px"><strong>65000</strong><span>PCs Repaired</span></div>
  <div class="stat" style="left:785px"><strong>2</strong><span>Companies</span></div>
</section>

<section class="plans">
  <h2 class="h2">Our Plans</h2>
  <div class="plan" style="left:245px"><header>PREMIUM</header><div class="price">$19.99 / MONTH</div><div class="sub">Billed yearly per device</div><div class="bar"></div><ul><li>Regular PC Tune-Up Optimization</li><li>Unlimited 24/7 Tech Support</li><li>Technician Support</li></ul><span class="btn-ghost">Learn More</span></div>
  <div class="plan featured" style="left:487px"><header>PLATINUM</header><div class="price">$39.99 / MONTH</div><div class="sub">Billed yearly per device</div><div class="bar"></div><ul><li>Regular PC Tune-Up Optimization</li><li>Unlimited 24/7 Tech Support</li><li>Technician Support</li><li>Online Identity Theft Protection</li></ul><span class="btn-ghost">Learn More</span></div>
  <div class="plan" style="left:725px"><header>PREMIUM PLUS</header><div class="price">$29.99 / MONTH</div><div class="sub">Billed yearly per device</div><div class="bar"></div><ul><li>Regular PC Tune-Up Optimization</li><li>Unlimited 24/7 Tech Support</li><li>Technician Support</li></ul><span class="btn-ghost">Learn More</span></div>
  <div class="pager abs">‹ 1 ›</div>
</section>

<section class="video">
  <div class="photo" role="img" aria-label="Support team at work, tinted blue"></div>
  <div class="play abs"><svg width="64" height="64" viewBox="0 0 64 64"><circle cx="32" cy="32" r="30" fill="none" stroke="#fff" stroke-width="2"/><path d="M26 20l18 12-18 12z" fill="#fff"/></svg><div style="margin-top:8px">Play Video</div></div>
</section>

<section class="partners">
  <svg class="abs" style="left:205px;top:62px" width="12" height="18" viewBox="0 0 12 18"><path d="M10 2L3 9l7 7" stroke="#9aa0a8" stroke-width="2" fill="none"/></svg>
  <div class="partner" style="left:250px"><i></i>Halvern</div>
  <div class="partner boxed" style="left:425px">Corlith</div>
  <div class="partner" style="left:600px"><i></i>Tessling</div>
  <div class="partner" style="left:775px"><i></i>Orbyte</div>
  <svg class="abs" style="left:985px;top:62px" width="12" height="18" viewBox="0 0 12 18"><path d="M2 2l7 7-7 7" stroke="#9aa0a8" stroke-width="2" fill="none"/></svg>
</section>

<section class="contact">
  <div class="photo" role="img" aria-label="Street map of the office neighbourhood"></div>
  <div class="contact-card abs">
    <h2>Get in touch</h2>
    <p class="small">Questions about a slow computer or a plan? Our team answers every message within a day.</p>
    <div class="line-item"><i></i>42 Harbor Lane, Suite 8, Eastfield</div>
    <div class="line-item"><i></i>(555) 014-2280</div>
    <div class="line-item"><i></i>info@brightdesk.com</div>
    <div class="socials"><i></i><i></i></div>
  </div>
</section>

<section class="form">
  <div class="field" style="left:240px;top:60px;width:355px">Name</div>
  <div class="field" style="left:610px;top:60px;width:350px">Email</div>
  <div class="field" style="left:240px;top:110px;width:720px;height:90px">Message</div>
  <div class="send abs">Send Message</div>
</section>

<section class="subscribe">
  <h2>Subscribe Us</h2>
  <p>Get tips, offers and news on keeping your computer running smoothly, straight to your inbox each month.</p>
  <div class="sub-input abs">Email Id</div>
  <div class="sub-btn abs">Subscribe</div>
</section>

<footer class="footer">Brightdesk © 2016. All Rights Reserved. Terms and Conditions · Refund Policy · Privacy Policy</footer>

</body>
</html>
```